Plumber needs a business card

I need a new business card for my plumbing business. I dont have a logo at the moment but I want business cards that are simple but very professional. I want to look like
Name: Milo Brenton
Address: (just make one up)
Phone: 0497 318 264
Email: milo@fernpost.net
Colors to use:
Blacks, blues, silvers

```html
<!DOCTYPE html>
<html lang="en">
<head>
<meta charset="utf-8">
<title>Milo Brenton – Business Card</title>
<link href="https://fonts.googleapis.com/css2?family=Open+Sans:wght@400;700&display=swap" rel="stylesheet">
<style>
  :root {
    --page-bg: #e9ebef;
    --card-blue-deep: #3346a8;
    --card-blue: #4359c4;
    --card-blue-light: #6c82d8;
    --ink-white: #ffffff;
    --ink-soft: #eef1fb;
  }
  * { box-sizing: border-box; margin: 0; padding: 0; }
  html, body {
    width: 1200px;
    height: 1023px;
    overflow: hidden;
    background: var(--page-bg);
    font-family: "Open Sans", Arial, sans-serif;
  }
  .stage {
    width: 1200px;
    height: 1023px;
    display: flex;
    align-items: center;
    justify-content: center;
  }
  .business-card {
    position: relative;
    width: 860px;
    height: 490px;
    border-radius: 34px;
    background: linear-gradient(160deg, var(--card-blue-light) 0%, var(--card-blue) 45%, var(--card-blue-deep) 100%);
    box-shadow: 0 18px 40px rgba(20, 30, 80, 0.28);
    color: var(--ink-white);
    overflow: hidden;
  }
  .brand-area {
    position: absolute;
    left: 0;
    top: 0;
    width: 380px;
    height: 100%;
    display: flex;
    align-items: center;
    justify-content: center;
  }
  .monogram {
    font-weight: 700;
    font-size: 140px;
    line-height: 1;
    letter-spacing: -2px;
    color: var(--ink-white);
    white-space: nowrap;
  }
  .divider {
    position: absolute;
    left: 380px;
    top: 0;
    width: 2px;
    height: 100%;
  }
  .details {
    position: absolute;
    left: 430px;
    top: 118px;
    right: 40px;
  }
  .holder-name {
    font-weight: 700;
    font-size: 38px;
    letter-spacing: -0.5px;
    margin-bottom: 26px;
  }
  .address {
    font-size: 22px;
    line-height: 1.35;
    color: var(--ink-soft);
    margin-bottom: 26px;
  }
  .contact-list { list-style: none; }
  .contact-list li {
    display: flex;
    align-items: center;
    gap: 12px;
    font-size: 22px;
    line-height: 1.45;
    color: var(--ink-soft);
  }
  .contact-list svg { width: 18px; height: 18px; flex: none; }
</style>
</head>
<body>
<main class="stage">
  <section class="business-card">
    <div class="brand-area">
      <div class="monogram">MB</div>
    </div>

    <svg class="divider" viewBox="0 0 2 490" preserveAspectRatio="none" aria-hidden="true">
      <defs>
        <linearGradient id="ruleFade" x1="0" y1="0" x2="0" y2="1">
          <stop offset="0" stop-color="#fff" stop-opacity="0"/>
          <stop offset="0.5" stop-color="#fff" stop-opacity="0.8"/>
          <stop offset="1" stop-color="#fff" stop-opacity="0"/>
        </linearGradient>
      </defs>
      <rect x="0" y="40" width="2" height="410" fill="url(#ruleFade)"/>
    </svg>

    <div class="details">
      <h1 class="holder-name">Milo Brenton</h1>
      <p class="address">Suite 102, Street name,<br>State, Zip 2034, Country</p>
      <ul class="contact-list">
        <li>
          <svg viewBox="0 0 18 18" aria-hidden="true"><rect x="4" y="1" width="10" height="16" rx="2" fill="#fff"/><rect x="6" y="3.5" width="6" height="9" fill="#4359c4"/></svg>
          000.000.0000
        </li>
        <li>
          <svg viewBox="0 0 18 18" aria-hidden="true"><path d="M4 2l3 3-2 2c1 2 3 4 5 5l2-2 3 3-2 3C7 16 2 11 1 5z" fill="#fff"/></svg>
          0497 318 264
        </li>
        <li>
          <svg viewBox="0 0 18 18" aria-hidden="true"><rect x="1" y="3" width="16" height="12" rx="1.5" fill="#fff"/><path d="M1.5 4l7.5 6 7.5-6" fill="none" stroke="#4359c4" stroke-width="1.6"/></svg>
          milo@fernpost.net
        </li>
      </ul>
    </div>
  </section>
</main>
</body>
</html>
```